Chiropody and Podiatry Flyer

A6 Flyer for a Chiropody Clinic.
Need to use an existing company logo (upload available).
Flyer should promote three aspects of the practice;
1) General chiropody : Nail Cutting; Corn Removal; Ingrown Nails; Hard Skin Removal; Verruca Treatment; Diabetic Assessment; Nail Surgery.
2) Home Visits - chiropody in the comfort of your own home.
3) Biomechanical Assessments / Orthotics
Colours should comprise navy blue/green/white to complement existing logo.
Promotional Offer on flyer.

Industry/Entity Type

Clinic

```html
<!DOCTYPE html>
<html lang="en">
<head>
<meta charset="utf-8">
<title>Kestrel Lane for Health – Chiropody Clinic Flyer</title>
<link rel="stylesheet" href="https://fonts.googleapis.com/css2?family=Tinos:wght@400;700&display=swap">
<style>
  :root {
    --navy-top: #0b4fa3;
    --navy-mid: #083a7a;
    --navy-deep: #03152f;
    --ink: #020b18;
    --green: #22d427;
    --white: #ffffff;
    --hours-blue: #0a55b5;
    --closed-red: #e0241f;
    --page-bg: #ffffff;
  }
  * { margin: 0; padding: 0; box-sizing: border-box; }
  html, body { width: 1200px; height: 830px; overflow: hidden; background: var(--page-bg); }
  body { position: relative; font-family: "Tinos", "Times New Roman", serif; color: var(--white); }

  .flyer {
    position: absolute; top: 47px; width: 519px; height: 733px; overflow: hidden;
    background: linear-gradient(to bottom, var(--navy-top) 0%, var(--navy-mid) 55%, var(--navy-deep) 78%, var(--ink) 100%);
  }
  .flyer--front { left: 78px; }
  .flyer--back { left: 616px; background: linear-gradient(to bottom, var(--navy-top) 0%, #0a4390 50%, #072a5c 80%, #041a3a 100%); }
  .flyer__art { position: absolute; left: 0; top: 0; width: 519px; }
  .flyer__base { position: absolute; left: 0; bottom: 0; width: 100%; height: 13px; background: var(--green); }

  .front__title {
    position: absolute; top: 396px; left: 0; width: 100%; text-align: center;
    font-size: 39px; line-height: 46px; font-weight: 700;
  }
  .brand {
    position: absolute; top: 540px; left: 0; width: 100%;
    display: flex; justify-content: center; align-items: center; gap: 12px;
  }
  .brand__dot { width: 16px; height: 16px; border-radius: 50%; background: var(--green); }
  .brand__name { font-size: 27px; font-weight: 400; letter-spacing: 1px; color: var(--white); }

  .contact { position: absolute; left: 140px; top: 628px; }
  .contact__row { display: flex; align-items: center; gap: 10px; height: 26px; font-size: 16px; }
  .contact__row--phone { font-size: 18px; font-weight: 700; height: 30px; }
  .contact__row svg { width: 14px; height: 14px; flex: none; }

  .services { position: absolute; left: 40px; top: 235px; width: 470px; height: 240px; }
  .services__heading { font-size: 17px; font-weight: 700; line-height: 22px; }
  .services__list { list-style: none; margin: 3px 0 0 26px; }
  .services__list li { font-size: 17px; line-height: 19.3px; position: relative; padding-left: 24px; }
  .services__list li::before { content: "•"; position: absolute; left: 0; }
  .services__heading--two { position: absolute; top: 177px; left: 0; white-space: nowrap; }
  .services__heading--three { position: absolute; top: 207px; left: 0; white-space: nowrap; }

  .address { position: absolute; left: 44px; top: 505px; display: flex; gap: 8px; }
  .address svg { width: 14px; height: 14px; margin-top: 2px; flex: none; }
  .address p { font-size: 15.5px; line-height: 17.6px; }

  .badge { position: absolute; left: 45px; background: var(--white); }
  .badge--society { top: 617px; width: 131px; height: 46px; }
  .badge--register { top: 669px; width: 131px; height: 26px; background: #dfe6f0; }

  .hours { position: absolute; left: 240px; top: 540px; width: 270px; }
  .hours__title { position: absolute; left: 98px; top: 2px; font-size: 14.5px; line-height: 18px; font-weight: 700; letter-spacing: 1px; white-space: nowrap; }
  .hours__table { position: absolute; left: 0; top: 29px; border-collapse: collapse; font-size: 15.5px; }
  .hours__table td { height: 17.5px; line-height: 17.5px; padding: 0; white-space: nowrap; }
  .hours__day { width: 101px; padding-left: 10px !important; position: relative; }
  .hours__day::before { content: ""; position: absolute; left: 0; top: 6px; width: 5px; height: 5px; border-radius: 50%; background: var(--green); }
  .hours__day--closed::before { background: var(--closed-red); }
</style>
</head>
<body>

<section class="flyer flyer--front">
  <svg class="flyer__art" height="400" viewBox="0 0 519 400">
    <defs>
      <linearGradient id="lakeScene" x1="0" y1="0" x2="0" y2="1">
        <stop offset="0" stop-color="#6f94c4"/>
        <stop offset="0.45" stop-color="#b7c9dc"/>
        <stop offset="0.55" stop-color="#8aa1b6"/>
        <stop offset="1" stop-color="#5f7f99"/>
      </linearGradient>
    </defs>
    <path role="img" aria-label="Photo: woman in white stretching her arms beside a calm mountain lake" d="M0 0 H519 V253 C420 340 280 392 160 388 C90 386 40 372 0 335 Z" fill="url(#lakeScene)"/>
    <path d="M0 335 C40 372 90 386 160 388 C280 392 420 340 519 253" fill="none" stroke="var(--green)" stroke-width="3"/>
  </svg>

  <h1 class="front__title">Chiropody Clinic</h1>

  <div class="brand">
    <span class="brand__dot"></span>
    <span class="brand__name">Kestrel Lane for Health</span>
  </div>

  <div class="contact">
    <div class="contact__row contact__row--phone">
      <svg viewBox="0 0 24 24"><path fill="var(--green)" d="M6.6 10.8a15.1 15.1 0 0 0 6.6 6.6l2.2-2.2a1 1 0 0 1 1-.25 11.4 11.4 0 0 0 3.6.57 1 1 0 0 1 1 1V20a1 1 0 0 1-1 1A17 17 0 0 1 3 4a1 1 0 0 1 1-1h3.5a1 1 0 0 1 1 1c0 1.25.2 2.45.57 3.57a1 1 0 0 1-.25 1z"/></svg>
      <span>01632 960418 | 07700 900527</span>
    </div>
    <div class="contact__row">
      <svg viewBox="0 0 24 24"><circle cx="12" cy="12" r="10" fill="none" stroke="var(--green)" stroke-width="2"/><path d="M2 12h20M12 2c3 3 3 17 0 20M12 2c-3 3-3 17 0 20" fill="none" stroke="var(--green)" stroke-width="1.6"/></svg>
      <span>www.kestrellaneforhealth.co.uk</span>
    </div>
    <div class="contact__row">
      <svg viewBox="0 0 24 24"><rect x="2" y="5" width="20" height="14" fill="none" stroke="var(--green)" stroke-width="2"/><path d="M2 5l10 8 10-8" fill="none" stroke="var(--green)" stroke-width="2"/></svg>
      <span>hello@kestrellaneforhealth.co.uk</span>
    </div>
  </div>

  <div class="flyer__base"></div>
</section>

<section class="flyer flyer--back">
  <svg class="flyer__art" height="733" viewBox="0 0 519 733">
    <defs>
      <linearGradient id="runnerScene" x1="0" y1="0" x2="0" y2="1"><stop offset="0" stop-color="#d9e3c9"/><stop offset="1" stop-color="#b85b4a"/></linearGradient>
      <linearGradient id="yogaScene" x1="0" y1="0" x2="0" y2="1"><stop offset="0" stop-color="#c6b69a"/><stop offset="1" stop-color="#5f5446"/></linearGradient>
      <linearGradient id="relaxScene" x1="0" y1="0" x2="0" y2="1"><stop offset="0" stop-color="#eef2f0"/><stop offset="1" stop-color="#b49a72"/></linearGradient>
      <clipPath id="photoStrip"><path d="M0 0 H519 V72 C430 180 300 210 180 205 C100 202 40 185 0 155 Z"/></clipPath>
    </defs>
    <g clip-path="url(#photoStrip)">
      <rect role="img" aria-label="Photo: runner kneeling to tie her trainer on a track" x="0" y="0" width="170" height="260" fill="url(#runnerScene)"/>
      <rect role="img" aria-label="Photo: woman in a yoga tree pose on a mountain top" x="170" y="0" width="152" height="260" fill="url(#yogaScene)"/>
      <rect role="img" aria-label="Photo: woman relaxing in a wicker lounge chair" x="322" y="0" width="197" height="260" fill="url(#relaxScene)"/>
    </g>
    <path d="M0 155 C40 185 100 202 180 205 C300 210 430 180 519 72" fill="none" stroke="var(--green)" stroke-width="4"/>
    <path d="M118 733 C140 640 230 525 376 505 C440 500 490 515 519 541 V733 Z" fill="var(--hours-blue)" opacity="0.85"/>
  </svg>

  <div class="services">
    <h2 class="services__heading">1) General chiropody</h2>
    <ul class="services__list">
      <li>Nail Cutting</li>
      <li>Corn Removal</li>
      <li>Ingrown Nails</li>
      <li>Hard Skin Removal</li>
      <li>Verruca Treatment</li>
      <li>Diabetic Assessment</li>
      <li>Nail Surgery</li>
    </ul>
    <h2 class="services__heading services__heading--two">2) Home Visits - chiropody in the comfort of your own home</h2>
    <h2 class="services__heading services__heading--three">3) Biomechanical Assessments / Orthotics</h2>
  </div>

  <div class="address">
    <svg viewBox="0 0 24 24"><path fill="var(--green)" d="M2 10 12 3l10 7v11H2zM6 13v5h5v-5zm7 0v5h5v-5z"/></svg>
    <p>4B, Orchard House<br>Millbrook Estate<br>Station Road<br>Eastwick, Colnford<br>Essex, CO9 2XY</p>
  </div>

  <div class="badge badge--society" role="img" aria-label="Professional society membership badge"></div>
  <div class="badge badge--register" role="img" aria-label="Professional registration badge"></div>

  <div class="hours">
    <h3 class="hours__title">WORKING HOURS</h3>
    <table class="hours__table">
      <tr><td class="hours__day">Monday</td><td>9:00 am - 8:00 pm</td></tr>
      <tr><td class="hours__day">Tuesday</td><td>9:00 am - 8:00 pm</td></tr>
      <tr><td class="hours__day">Wednesday</td><td>9:00 am - 6:30 pm</td></tr>
      <tr><td class="hours__day">Thursday</td><td>9:00 am - 8:00 pm</td></tr>
      <tr><td class="hours__day">Friday</td><td>9:00 am - 4:00 pm</td></tr>
      <tr><td class="hours__day">Saturday</td><td>9:00 am - 1:00 pm</td></tr>
      <tr><td class="hours__day hours__day--closed">Sunday</td><td>Closed</td></tr>
    </table>
  </div>

  <div class="flyer__base"></div>
</section>

</body>
</html>
```